Website Design for Chef Varo Chinese Restaurant

Chef Varo is a new Chinese Restaurant. It offers exceptional dining experience with authentic and dynamic dishes created with quality ingredients.

A vivid website theme is required to promote this new restaurant online. Logo, menu, wine list and a few other files are attached for help with designing.

A very rough demo website has been setup and can be accessed via http://www.chefvaro.com.au. It is for telling designers what content is shown up on each page (except for homepage). By reading the about us page, designers can get some more info of Chef Varo. However, the layout, theme color, font, etc are not set in stone. Visitors should be able to feel Chef Varo restaurant's authentic Chinese cuisine and high hygiene standard. Home page of the website could be The "Our website is coming soon" description is shown on demo site but do not required to be presented on new design.

Some main pages design should be included: Home (landing page), About us, Menu (Dishes), Winelist, Gallery, Contact us. No HTML and coding required. The output should be well layered psd or png files with acceptable resolution for web use.

A few other website can be referred to are:

http://belmiraeatery.com.au/
http://www.stone-kettle.com/
http://quillhaven.com.au/
http://meadowbistro.com.au/
http://www.lanternvaledining.com.au/
http://www.thetrove.com.au/

Industry/Entity Type

Restaurant

Requirements
Nice to have
• I expect designs of at least these webpages: homepage, menu page and contact us page. If you can provide "about us" page as well, it will probably help you win the competition. well layered psd or png file is my preference.
Should not have
• You don't have to make html/cs/js or any coding. All I need is just art design

```html
<!DOCTYPE html>
<html lang="en">
<head>
<meta charset="utf-8">
<title>Chef Varo Chinese Restaurant</title>
<link rel="stylesheet" href="https://fonts.googleapis.com/css2?family=Arimo:wght@400;700&family=Cormorant+Garamond:ital,wght@1,500&display=swap">
<style>
  :root {
    --red: #e8200a;
    --red-bright: #ee0a0a;
    --red-text: #e31a0b;
    --cream: #fffbd0;
    --logo-cream: #fdf8c9;
    --charcoal: #3a3a3a;
    --topbar: #6b6b6b;
    --footer: #2b2b2b;
    --ink: #222;
    --white: #fff;
  }
  * { box-sizing: border-box; margin: 0; padding: 0; }
  html, body { width: 923px; height: 1200px; overflow: hidden; }
  body { position: relative; font-family: "Arimo", Arial, sans-serif; background: var(--cream); color: var(--ink); }
  .abs { position: absolute; }

  .topbar { left: 0; top: 0; width: 923px; height: 33px; background: var(--topbar); }
  .reservation { left: 66px; top: 8px; color: var(--white); font-size: 12px; font-weight: 700; display: flex; align-items: center; gap: 6px; }
  .social { right: 70px; top: 8px; display: flex; gap: 18px; }
  .social span { width: 16px; height: 16px; border-radius: 50%; background: var(--white); display: block; }
  .social span:first-child { background: var(--red); }

  .navbar { left: 0; top: 33px; width: 923px; height: 63px; background: var(--charcoal); }
  .nav-link { top: 53px; font-size: 14.5px; color: var(--red-text); text-decoration: none; }
  .nav-link.active { color: var(--white); }

  .hero { left: 0; top: 96px; width: 923px; height: 429px; background: radial-gradient(ellipse at center, #ee2a10 0%, var(--red) 60%, #d81a06 100%); }

  .brand-badge { left: 370px; top: 3px; width: 182px; height: 182px; border-radius: 50%; background: var(--logo-cream); border: 8px solid var(--charcoal); display: flex; flex-direction: column; align-items: center; justify-content: center; gap: 4px; }
  .brand-name { font-size: 22px; font-weight: 700; color: var(--red-text); }
  .brand-sub { font-size: 8px; font-weight: 700; color: var(--red-text); letter-spacing: .2px; }

  .dish { border-radius: 50%; border: 6px solid var(--logo-cream); }
  .dish.center { border: 8px solid var(--charcoal); }

  .welcome-photo { left: 59px; top: 540px; width: 241px; height: 240px; background: linear-gradient(135deg, #6d4a2c 0%, #b88a5a 45%, #e9dcc4 75%, #8a6a44 100%); }
  .welcome-card { left: 300px; top: 540px; width: 563px; height: 240px; background: var(--white); }
  .ribbon { width: 48px; height: 57px; }
  .welcome-title { left: 385px; top: 552px; font-size: 22px; color: var(--red-text); }
  .welcome-text { left: 316px; top: 590px; width: 530px; font-size: 10.4px; line-height: 17.6px; color: #333; }
  .welcome-text p + p { margin-top: 17.6px; }
  .read-more { left: 741px; top: 738px; width: 96px; height: 32px; background: var(--red-bright); color: var(--white); font-size: 12px; font-weight: 700; display: flex; align-items: center; justify-content: center; border-radius: 2px; }

  .wine-card { top: 804px; width: 257px; height: 200px; background: var(--white); }
  .wine-title { font-size: 16px; color: var(--ink); }
  .wine-list { list-style: none; font-size: 13px; font-weight: 700; color: var(--red-text); }
  .wine-list li { height: 24px; }
  .wine-list.tight li { height: 21.6px; }

  .hours { left: 0; top: 1016px; width: 923px; height: 111px; background: var(--red-bright); color: var(--white); }
  .hours-badge { left: 60px; top: 5px; width: 94px; height: 94px; border-radius: 50%; background: var(--white); border: 3px solid #f2d7d2; box-shadow: inset 0 0 8px rgba(0,0,0,.15); display: flex; align-items: center; justify-content: center; text-align: center; font-family: "Cormorant Garamond", Georgia, serif; font-style: italic; font-size: 20px; line-height: 23px; color: var(--red-text); }
  .open-days { left: 170px; top: 32px; width: 140px; text-align: center; font-size: 19px; line-height: 24px; }
  .hours-col { top: 22px; width: 260px; text-align: center; font-size: 12.4px; }
  .hours-col h3 { font-weight: 400; font-size: 15.5px; margin-bottom: 9px; }
  .hours-col p { line-height: 25px; }

  .footer { left: 0; top: 1127px; width: 923px; height: 73px; background: var(--footer); border-top: 1px solid #555; }
  .foot-link { top: 1138px; font-size: 12.8px; color: var(--white); }
  .foot-link.active { color: var(--red-text); }
  .copyright { left: 0; top: 1169px; width: 923px; text-align: center; font-size: 10.5px; color: var(--white); }
  .copyright span { color: var(--red-text); }
</style>
</head>
<body>

<div class="abs topbar"></div>
<div class="abs reservation">
  <svg width="16" height="16" viewBox="0 0 24 24"><path fill="#fff" d="M6.6 10.8a15.1 15.1 0 0 0 6.6 6.6l2.2-2.2a1 1 0 0 1 1-.25 11.4 11.4 0 0 0 3.6.57 1 1 0 0 1 1 1V20a1 1 0 0 1-1 1A17 17 0 0 1 3 4a1 1 0 0 1 1-1h3.5a1 1 0 0 1 1 1c0 1.25.2 2.45.57 3.57a1 1 0 0 1-.25 1z"/></svg>
  Make a Reservation : +44 120 555 0148
</div>
<div class="abs social" aria-label="Social links"><span></span><span></span><span></span><span></span><span></span></div>

<div class="abs navbar"></div>
<a class="abs nav-link active" style="left:70px">Home</a>
<a class="abs nav-link" style="left:144px">About</a>
<a class="abs nav-link" style="left:221px">Menu</a>
<a class="abs nav-link" style="left:294px">Winelist</a>
<a class="abs nav-link" style="left:575px">Facilities</a>
<a class="abs nav-link" style="left:679px">Events</a>
<a class="abs nav-link" style="left:769px">Contact</a>

<section class="abs hero">
  <div class="abs dish" role="img" aria-label="Sliced salmon sashimi" style="left:22px;top:151px;width:176px;height:176px;background:radial-gradient(circle at 45% 45%,#f45a3a,#e23a22 55%,#f3efe8 90%)"></div>
  <div class="abs dish" role="img" aria-label="Pan-fried turnip cakes" style="left:156px;top:136px;width:224px;height:224px;background:radial-gradient(circle at 40% 50%,#e0a45a,#c98a40 45%,#f4efe6 80%)"></div>
  <div class="abs dish" role="img" aria-label="Prawn dumplings on noodles" style="left:541px;top:136px;width:224px;height:224px;background:radial-gradient(circle at 50% 45%,#f2d7c4,#e8bfa0 50%,#d9c27a 85%)"></div>
  <div class="abs dish" role="img" aria-label="Steamed crab with ginger" style="left:717px;top:151px;width:176px;height:176px;background:radial-gradient(circle at 50% 35%,#e8412a,#d7512e 45%,#e6c9a0 85%)"></div>
  <div class="abs dish center" role="img" aria-label="Steamed sponge cake" style="left:333px;top:112px;width:256px;height:256px;background:radial-gradient(circle at 50% 48%,#c8683a,#b95a30 45%,#f3f1ee 75%)"></div>
</section>

<div class="abs brand-badge">
  <span class="brand-name">Chef Varo</span>
  <span class="brand-sub">CHEF VARO CHINESE RESTAURANT</span>
</div>

<div class="abs welcome-photo" role="img" aria-label="Restaurant dining room interior"></div>
<div class="abs welcome-card"></div>
<svg class="abs ribbon" style="left:308px;top:532px;width:64px" viewBox="0 0 64 57">
  <path fill="#a40c00" d="M0 8 L8 0 L8 8 Z M56 0 L64 8 L56 8 Z"/>
  <path fill="#e8200a" d="M8 0 H56 V57 L32 46 L8 57 Z"/>
  <path fill="#fff" d="M32 15 L44 25 H40 V34 H35 V28 H29 V34 H24 V25 H20 Z"/>
</svg>
<h1 class="abs welcome-title">Welcome to &nbsp;Chef Varo</h1>
<div class="abs welcome-text">
  <p>Chef Varo is named after its' executive chef, Mr. Varo. Chef Varo has been in his career for nearly two decades before he moved to Australia nine years ago. He settled in Adelaide then started his first restaurant, Lotus Terrace in Norwood. Lotus Terrace has been running successfully for years due to Chef Varo's talent of cooking.</p>
  <p>We offer an exceptional dining experience with authentic and dynamic dishes created with quality ingredients. The menu of Chef Varo is based on classic Cantonese dishes, featured by southern China's local flavour characteristics. Taking advantage of South Australia's rich and quality food resources...</p>
</div>
<div class="abs read-more">READ MORE</div>

<div class="abs wine-card" style="left:59px"></div>
<svg class="abs ribbon" style="left:67px;top:796px;width:64px" viewBox="0 0 64 57">
  <path fill="#a40c00" d="M0 8 L8 0 L8 8 Z M56 0 L64 8 L56 8 Z"/>
  <path fill="#e8200a" d="M8 0 H56 V57 L32 46 L8 57 Z"/>
  <path fill="#fff" d="M22 20 L40 12 L42 17 L26 24 Z M24 26 L28 26 L28 38 L24 38 Z"/>
</svg>
<div class="abs wine-title" style="left:139px;top:825px">WINES</div>
<ul class="abs wine-list" style="left:139px;top:852px">
  <li>Champagne</li><li>Sparkling White</li><li>Sparkling Red</li>
</ul>

<div class="abs wine-card" style="left:332px"></div>
<svg class="abs ribbon" style="left:340px;top:796px;width:64px" viewBox="0 0 64 57">
  <path fill="#a40c00" d="M0 8 L8 0 L8 8 Z M56 0 L64 8 L56 8 Z"/>
  <path fill="#e8200a" d="M8 0 H56 V57 L32 46 L8 57 Z"/>
  <circle cx="36" cy="20" r="8" fill="none" stroke="#fff" stroke-width="2.5"/>
  <path stroke="#fff" stroke-width="2.5" d="M31 26 L20 38 M16 35 L24 42"/>
</svg>
<div class="abs wine-title" style="left:407px;top:814px">WHITE WINE</div>
<ul class="abs wine-list" style="left:407px;top:852px">
  <li>Riesling</li><li>Pinot Gris / Pinot Grigio</li><li>Sauvignon Blanc and Blends</li><li>Chardonnay</li><li>Other White Varietals</li>
</ul>

<div class="abs wine-card" style="left:604px"></div>
<svg class="abs ribbon" style="left:612px;top:796px;width:64px" viewBox="0 0 64 57">
  <path fill="#a40c00" d="M0 8 L8 0 L8 8 Z M56 0 L64 8 L56 8 Z"/>
  <path fill="#e8200a" d="M8 0 H56 V57 L32 46 L8 57 Z"/>
  <path fill="none" stroke="#fff" stroke-width="2" d="M22 10 H30 V20 A4 4 0 0 1 22 20 Z M34 10 H42 V20 A4 4 0 0 1 34 20 Z M26 24 V36 M38 24 V36 M22 36 H30 M34 36 H42"/>
</svg>
<div class="abs wine-title" style="left:680px;top:822px">RED WINE</div>
<ul class="abs wine-list tight" style="left:677px;top:849px">
  <li>Rosé</li><li>Pinot Noir</li><li>Grenache/Sangiovese/Merlot</li><li>Cabernet Sauvignon &amp; Blends</li><li>Shiraz and Blends</li><li>Other Red Varietals</li>
</ul>

<section class="abs hours">
  <div class="abs hours-badge">Opening<br>Hours</div>
  <div class="abs open-days">We are open<br>7 days</div>
  <div class="abs hours-col" style="left:326px">
    <h3>Lunch :</h3>
    <p>Monday to Friday 11:30am – 2:30pm</p>
    <p>Saturday to Sunday 11:00am – 3:00pm</p>
  </div>
  <div class="abs hours-col" style="left:604px">
    <h3>Dinner :</h3>
    <p>Monday to Sunday 6:00pm Until Late</p>
  </div>
</section>

<footer class="abs footer"></footer>
<a class="abs foot-link active" style="left:172px">Home</a>
<a class="abs foot-link" style="left:249px">About</a>
<a class="abs foot-link" style="left:334px">Menu</a>
<a class="abs foot-link" style="left:412px">Winelist</a>
<a class="abs foot-link" style="left:512px">Facilities</a>
<a class="abs foot-link" style="left:616px">Events</a>
<a class="abs foot-link" style="left:706px">Contact</a>
<div class="abs copyright">© <span>Chef Varo</span> - 2014. All Rights Reserved.</div>

</body>
</html>
```